Dr. Lumora needs a design for its website!

*Only need the design, coding is not required.
*Need desktop version ($500) and mobile/tablet version ($200)
*The attached files are not the exact layout we want, they are just for you to know what information should be included in those pages.
*The function of our website is like www.qavlo.hk
*For the background picture, prefer a lively picture and chinese people in it, NOT necessarily need a doctor or sick person in the picture

***Don't just copy the layout from the attachments or from the reference website, we are looking for creative ideas, non-ordinary designs!!!****

We are developing a website for the public to search a doctor by different criteria. At the initial stage, we need 4 pages to start with and other pages at later stage. I have attached the general idea of these pages but not necessarily to be exactly the same, I am looking for some new ideas.

This website needs a professional, modern, simple and user friendly design. The main color to be used in the website will be same as the color (R:0 G:139 B:205) used in our logo (see attached). We don't have any particular thoughts for the other color and the font to be used in the website. Can try to use circle outline for the icon in the navigation bar.

1. Home: will include 4 sections (see attached)

2. Doctor's details (see attached)

3. Health information: will include a short descriptions of this Health Info page and 5 sections (see attached)

4. News (see attached)

Reason: Not too many suitable designs to choose from and need more time to go through the designs

All

Medical

4 page

• must not be same as or looks too much like www.qavlo.hk
• prefer not to use black and red color

```html
<!DOCTYPE html>
<html lang="en">
<head>
<meta charset="utf-8">
<title>Dr. Lumora – Find a Doctor</title>
<link rel="stylesheet" href="https://fonts.googleapis.com/css2?family=Open+Sans:wght@400;600&family=Raleway:wght@400;500&display=swap">
<style>
:root{
  --brand:#008bcd;
  --brand-dark:#0679b5;
  --ink:#333;
  --text:#3a3a3a;
  --muted:#777;
  --line:#d9d9d9;
  --soft:#f5f5f5;
  --white:#fff;
}
*{box-sizing:border-box;margin:0;padding:0}
html,body{width:1200px;height:1044px;overflow:hidden;background:var(--white)}
body{position:relative;font-family:'Raleway',sans-serif;color:var(--text)}
.abs{position:absolute}
.top-line{left:0;top:0;width:1200px;height:2px;background:var(--brand)}
.brand{left:160px;top:24px;display:flex;align-items:center;gap:8px}
.brand-dot{width:40px;height:40px;border-radius:50%;background:var(--brand)}
.brand-name{font-family:'Open Sans',sans-serif;font-weight:600;font-size:27px;color:var(--brand);letter-spacing:-.5px}
.social{display:flex;gap:10px}
.social span{display:block;border-radius:50%;background:var(--brand)}
.social.head{left:763px;top:31px}
.social.head span{width:28px;height:28px}
.lang{left:924px;top:27px;width:114px;height:35px;border-radius:18px;background:#f1f1f1;border:1px solid #ddd;display:flex;align-items:center;gap:8px;padding-left:8px;font-family:'Open Sans',sans-serif;font-size:13px;color:var(--ink)}
.lang .flag{width:22px;height:22px;border-radius:50%;background:#c9d3e6}
.nav{left:0;top:87px;width:1200px;height:41px;background:var(--brand)}
.nav a{position:absolute;top:0;line-height:41px;color:var(--white);font-family:'Open Sans',sans-serif;font-size:13.5px;text-decoration:none;letter-spacing:.2px}
.nav .sep{position:absolute;top:12px;width:1px;height:18px;background:rgba(255,255,255,.35)}
.nav .active::after{content:"";position:absolute;left:-8px;right:-8px;bottom:6px;height:6px;border-radius:50%;background:rgba(255,255,255,.25)}
.nav-search{position:absolute;left:855px;top:0;width:183px;height:41px;background:var(--brand-dark);color:var(--white);font-family:'Open Sans',sans-serif;font-size:14px;display:flex;align-items:center;gap:10px;padding-left:18px}
.panel{border:1px solid var(--line);background:var(--white)}
.panel-head{position:absolute;left:-1px;right:-1px;top:-1px;height:45px;background:var(--brand);color:var(--white);font-family:'Open Sans',sans-serif;font-size:16.5px;display:flex;align-items:center}
.panel-head.center{justify-content:center;gap:10px}
.pin{width:18px;height:18px;border-radius:50%;background:rgba(255,255,255,.3)}
.notch{position:absolute;bottom:-6px;left:50%;margin-left:-7px;width:0;height:0;border-left:7px solid transparent;border-right:7px solid transparent;border-bottom:7px solid var(--white)}
.label{position:absolute;font-size:12px;color:var(--text)}
.field{position:absolute;border:1px solid #cfcfcf;height:30px;font-size:10px;color:var(--muted);padding-left:15px;line-height:28px;background:var(--white)}
.field .caret{position:absolute;right:0;top:0;width:39px;height:28px;border-left:1px solid #cfcfcf}
.field .caret::after{content:"";position:absolute;left:14px;top:12px;border-left:5px solid transparent;border-right:5px solid transparent;border-top:5px solid var(--ink)}
.btn{position:absolute;color:var(--white);font-size:13px;display:flex;align-items:center;justify-content:center;gap:6px}
.btn.dark{background:var(--ink)}
.btn.blue{background:var(--brand)}
.perks{position:absolute;left:29px;top:75px;list-style:none}
.perks li{font-size:12px;height:23.4px;display:flex;align-items:center;gap:9px}
.decor{position:absolute;left:268px;top:54px;width:138px;height:188px;border-radius:69px 69px 40px 40px;background:#f4f4f4}
.radio{display:inline-block;width:11px;height:11px;border:1px solid #999;border-radius:50%;vertical-align:-1px;margin:0 5px 0 12px}
table{position:absolute;left:0;top:44px;width:824px;border-collapse:collapse;font-size:11.5px}
th{height:42px;background:var(--soft);font-family:'Open Sans',sans-serif;font-weight:400;font-size:11.5px;color:var(--ink)}
td{height:37.6px;text-align:center;border-top:1px solid #e4e4e4;line-height:1.25}
th+th,td+td{border-left:1px solid #e4e4e4}
th:first-child,td:first-child{text-align:left;padding-left:24px}
.person{display:inline-block;width:9px;height:20px;border-radius:4px;background:var(--ink);vertical-align:middle}
.footer{left:0;top:1002px;width:1200px;height:42px;background:var(--brand);color:var(--white);font-family:'Open Sans',sans-serif;font-size:11.5px}
.footer p{position:absolute;left:190px;top:14px}
.social.foot{position:absolute;left:894px;top:9px;gap:8px}
.social.foot span{width:24px;height:24px;background:var(--white)}
</style>
</head>
<body>
<div class="abs top-line"></div>

<header>
  <div class="abs brand"><span class="brand-dot"></span><span class="brand-name">Dr. Lumora</span></div>
  <div class="abs social head" aria-label="Social links"><span></span><span></span><span></span><span></span></div>
  <div class="abs lang"><span class="flag" role="img" aria-label="Language flag"></span>English
    <svg width="10" height="6" viewBox="0 0 10 6"><path d="M1 1l4 4 4-4" fill="none" stroke="#333" stroke-width="1.5"/></svg>
  </div>
  <nav class="abs nav">
    <a class="active" style="left:169px">HOME</a>
    <span class="sep" style="left:248px"></span>
    <a style="left:277px">(TBC)</a>
    <span class="sep" style="left:341px"></span>
    <a style="left:370px">HEALTH INFO</a>
    <span class="sep" style="left:490px"></span>
    <a style="left:519px">NEWS</a>
    <span class="sep" style="left:588px"></span>
    <a style="left:617px">ABOUT US</a>
    <span class="sep" style="left:715px"></span>
    <a style="left:744px">CONTACT US</a>
    <div class="nav-search">
      <svg width="15" height="15" viewBox="0 0 15 15"><circle cx="6" cy="6" r="4.8" fill="none" stroke="#fff" stroke-width="2"/><path d="M9.5 9.5l4 4" stroke="#fff" stroke-width="2.2"/></svg>Search
    </div>
  </nav>
</header>

<section class="abs panel login" style="left:188px;top:158px;width:368px;height:250px">
  <div class="panel-head center"><span class="pin"></span>Member Login<span class="notch"></span></div>
  <span class="label" style="left:23px;top:64px">Login Email</span>
  <div class="field" style="left:23px;top:83px;width:322px">Email</div>
  <span class="label" style="left:23px;top:127px">Password</span>
  <div class="field" style="left:23px;top:147px;width:322px">Password</div>
  <span class="label" style="left:23px;top:202px;font-size:12.5px">Forgot Password</span>
  <div class="btn dark" style="left:135px;top:192px;width:210px;height:37px">Log in</div>
</section>

<section class="abs panel member" style="left:586px;top:158px;width:428px;height:250px">
  <div class="panel-head" style="padding-left:24px">Become a Dr. Lumora Member
    <span class="pin" style="position:absolute;right:22px"></span></div>
  <div class="decor" role="img" aria-label="Faint doctor illustration"></div>
  <ul class="perks">
    <li><svg width="11" height="10" viewBox="0 0 11 10"><path d="M1 5l3 3 6-7" fill="none" stroke="#008bcd" stroke-width="2"/></svg>First Hand Health News</li>
    <li><svg width="11" height="10" viewBox="0 0 11 10"><path d="M1 5l3 3 6-7" fill="none" stroke="#008bcd" stroke-width="2"/></svg>Exclusive Promotions</li>
    <li><svg width="11" height="10" viewBox="0 0 11 10"><path d="M1 5l3 3 6-7" fill="none" stroke="#008bcd" stroke-width="2"/></svg>Instant Health Advices</li>
    <li><svg width="11" height="10" viewBox="0 0 11 10"><path d="M1 5l3 3 6-7" fill="none" stroke="#008bcd" stroke-width="2"/></svg>Free Health Seminars/Talks</li>
    <li><svg width="11" height="10" viewBox="0 0 11 10"><path d="M1 5l3 3 6-7" fill="none" stroke="#008bcd" stroke-width="2"/></svg>Priority Doctor Appointments</li>
  </ul>
  <div class="btn dark" style="left:26px;top:191px;width:105px;height:37px">And More
    <svg width="6" height="9" viewBox="0 0 6 9"><path d="M1 1l3.5 3.5L1 8" fill="none" stroke="#fff" stroke-width="1.5"/></svg></div>
</section>

<section class="abs panel search-form" style="left:188px;top:438px;width:826px;height:289px">
  <span class="label" style="left:23px;top:18px">Doctor’s Name</span>
  <div class="field" style="left:23px;top:37px;width:589px">doctor’s name</div>
  <span class="label" style="left:631px;top:45px">Gender :<span class="radio"></span>Male<span class="radio"></span>Female</span>
  <span class="label" style="left:23px;top:82px">Specialism</span>
  <div class="field" style="left:23px;top:101px;width:375px">select<span class="caret"></span></div>
  <span class="label" style="left:428px;top:82px">Symptoms</span>
  <div class="field" style="left:428px;top:101px;width:374px">select<span class="caret"></span></div>
  <span class="label" style="left:23px;top:142px">District</span>
  <div class="field" style="left:23px;top:161px;width:375px">Select<span class="caret"></span></div>
  <span class="label" style="left:428px;top:142px">Phone Number</span>
  <div class="field" style="left:428px;top:161px;width:374px">phone number<span class="caret"></span></div>
  <div class="btn dark" style="left:23px;top:206px;width:375px;height:37px">Reset</div>
  <div class="btn blue" style="left:427px;top:206px;width:375px;height:37px">Search
    <svg width="12" height="12" viewBox="0 0 12 12"><circle cx="5" cy="5" r="3.8" fill="none" stroke="#fff" stroke-width="1.7"/><path d="M7.8 7.8l3 3" stroke="#fff" stroke-width="1.9"/></svg></div>
</section>

<svg class="abs" style="left:985px;top:660px" width="90" height="120" viewBox="0 0 90 120">
  <path d="M5 5C60 25 105 70 50 110" fill="none" stroke="#008bcd" stroke-width="1.3"/>
  <path d="M46 101l0 11 10-3z" fill="#008bcd"/>
</svg>

<section class="abs panel results" style="left:188px;top:756px;width:826px;height:202px">
  <div class="panel-head center"><span class="pin"></span>Search Result<span class="notch" style="border-bottom-color:#f5f5f5"></span></div>
  <table>
    <colgroup><col style="width:187px"><col style="width:69px"><col style="width:100px"><col style="width:82px"><col style="width:64px"><col style="width:143px"><col style="width:73px"><col></colgroup>
    <tr><th>NAME</th><th>GENDER</th><th>SPECIALISM</th><th>SYMPTOS</th><th>LOREM</th><th>ADDRESS</th><th>DISTRICT</th><th>PHONE NO</th></tr>
    <tr><td>Lorem Ipsum is simply</td><td><span class="person" role="img" aria-label="Male"></span></td><td>Lorem Ipsum</td><td>Private</td><td>Dummy</td><td>dummy text of<br>the printing and</td><td>Dummy</td><td>21234567</td></tr>
    <tr><td>Lorem Ipsum is simply</td><td><span class="person" role="img" aria-label="Female"></span></td><td>Lorem Ipsum</td><td>Private</td><td>Dummy</td><td>dummy text of<br>the printing and</td><td>Dummy</td><td>21234568</td></tr>
    <tr><td>Lorem Ipsum is simply</td><td><span class="person" role="img" aria-label="Male"></span></td><td>Lorem Ipsum</td><td>Private</td><td>Dummy</td><td>dummy text of<br>the printing and</td><td>Dummy</td><td>21234567</td></tr>
  </table>
</section>

<footer class="abs footer">
  <p>Copyright © 2016 Dr. Lumora. All Right Reserved.</p>
  <div class="social foot" aria-label="Social links"><span></span><span></span><span></span><span></span></div>
</footer>
</body>
</html>
```